MR Business Card

I want to create a simple business card.
I am a consultant. I design and develop furniture, lighting and accessories for hospitality and retail brands.
I want the card to be simple and clean. Not too much of a logo - but it needs the basic information shown on the attached file.
Also - I have shown some fonts that I like on the attached file.
The card can be square or rectangle. It should be double sided.
I prefer 1-2 colors (not too colorful - but using color an an accent) Even if using color on the edges as an accent.

My snapgrove link shows some other graphics styles that I like. I like clean and simple.
http://www.snapgrove-boards.net/marenrosko/business-cards/

```html
<!DOCTYPE html>
<html lang="en">
<head>
<meta charset="utf-8">
<title>Maren Rosko — Business Card</title>
<link href="https://fonts.googleapis.com/css2?family=Cabin:wght@400;600&family=Arimo:wght@400&display=swap" rel="stylesheet">
<style>
  :root {
    --bg: #2e2c30;
    --card-front: #fafafa;
    --card-back: #e8e8e8;
    --ink: #2b2b2b;
    --rule: #6a6a6a;
    --ornament: #8a8a8a;
    --dot: #666666;
  }
  * { margin: 0; padding: 0; box-sizing: border-box; }
  html, body { width: 1000px; height: 1200px; overflow: hidden; }
  body { background: var(--bg); position: relative; font-family: "Cabin", sans-serif; color: var(--ink); }

  .card { position: absolute; width: 723px; height: 423px; }
  .card--front { left: 145px; top: 95px; background: var(--card-front); }
  .card--back { left: 126px; top: 652px; background: var(--card-back); }

  .frame { position: absolute; left: 0; top: 0; }
  .corner-ornament { position: absolute; width: 30px; height: 30px; background: var(--ornament); opacity: .35; }

  .contact { position: absolute; right: 70px; top: 76px; font-family: "Arimo", sans-serif; font-size: 20px; text-align: right; }
  .contact__line { display: flex; justify-content: flex-end; align-items: center; height: 32px; gap: 9px; }
  .contact__icon { width: 16px; height: 16px; }

  .identity { position: absolute; }
  .identity__name { font-weight: 600; line-height: 1; white-space: nowrap; }
  .identity__tagline { font-weight: 400; line-height: 1; white-space: nowrap; }

  .card--front .identity { left: 68px; top: 300px; }
  .card--front .identity__name { font-size: 36px; }
  .card--front .identity__tagline { font-size: 19px; margin-top: 10px; }

  .card--back .identity { left: 0; right: 0; top: 140px; text-align: center; }
  .card--back .identity__name { font-size: 52px; }
  .card--back .identity__tagline { font-size: 26px; margin-top: 12px; }

  .services { position: absolute; left: 0; right: 0; top: 276px; text-align: center; font-family: "Arimo", sans-serif; font-size: 21px; letter-spacing: .12em; white-space: nowrap; }
  .services__dot { display: inline-block; width: 6px; height: 6px; border-radius: 50%; background: var(--dot); vertical-align: middle; margin: 0 12px 3px; }
</style>
</head>
<body>
  <section class="card card--front" aria-label="Card front">
    <svg class="frame" width="723" height="423" aria-hidden="true">
      <g stroke="var(--rule)" stroke-width="1.2">
        <line x1="60" y1="34" x2="663" y2="34"/>
        <line x1="60" y1="389" x2="663" y2="389"/>
        <line x1="36" y1="58" x2="36" y2="366"/>
        <line x1="688" y1="58" x2="688" y2="366"/>
      </g>
    </svg>
    <div class="corner-ornament" role="img" aria-label="Corner flourish ornament" style="left:21px;top:20px"></div>
    <div class="corner-ornament" role="img" aria-label="Corner flourish ornament" style="left:673px;top:20px"></div>
    <div class="corner-ornament" role="img" aria-label="Corner flourish ornament" style="left:21px;top:372px"></div>
    <div class="corner-ornament" role="img" aria-label="Corner flourish ornament" style="left:673px;top:372px"></div>

    <div class="contact">
      <div class="contact__line">maren@marenrosko.com
        <svg class="contact__icon" viewBox="0 0 16 16" aria-hidden="true"><rect x="1" y="3.5" width="14" height="10" fill="var(--ink)"/><path d="M1.5 4 L8 9.5 L14.5 4" fill="none" stroke="var(--card-front)" stroke-width="1.3"/></svg>
      </div>
      <div class="contact__line">917.555.0148
        <svg class="contact__icon" viewBox="0 0 16 16" aria-hidden="true"><path d="M4 1.5 L6.5 4.5 L5 6.5 C6 8.5 7.5 10 9.5 11 L11.5 9.5 L14.5 12 L12.5 14.5 C7 14 2 9 1.5 3.5 Z" fill="var(--ink)"/></svg>
      </div>
    </div>

    <div class="identity">
      <p class="identity__name">Maren Rosko</p>
      <p class="identity__tagline">hospitality and home</p>
    </div>
  </section>

  <section class="card card--back" aria-label="Card back">
    <div class="identity">
      <p class="identity__name">Maren Rosko</p>
      <p class="identity__tagline">hospitality and home</p>
    </div>
    <p class="services">ff&amp;e<span class="services__dot"></span>furniture<span class="services__dot"></span>lighting<span class="services__dot"></span>textiles etc</p>
  </section>
</body>
</html>
```